b-ryx design for startup inpection service

building and pest inspections what i had in mind was b-ryx in large print with prepurchase in small print directly under it and the small tm (tradmark) .Within the C I would like an eye but I don't want to take away from the C so maybe the eye would be done in a fine line?I would also like the Building and Pest inspections to be prominent and large .Have no idea of colors but do like black orange and silver

Target Market(s)

home buyers and realestate agents

Industry/Entity Type

Building

Contact Information for Business Card

b-ryx prepurchase, Phone 0413926058, fax 02 93514770, email b-ryx@mailnest.com.au ,building and pest inspections

Font styles to use
Sans Serif

Requirements
Must have
• bold color
• simple layout
• bold color
• uncluttered layout
Should not have
• contact details the same size as Building and Pest Inspections

```html
<!DOCTYPE html>
<html lang="en">
<head>
<meta charset="utf-8">
<title>b-ryx prepurchase – business cards</title>
<link rel="stylesheet" href="https://fonts.googleapis.com/css2?family=Ubuntu:wght@400;500;700&family=Fira+Sans+Extra+Condensed:wght@600&display=swap">
<style>
  :root {
    --backdrop: #5c1012;
    --card: #ffffff;
    --navy: #0c1a2a;
    --ink: #0d2d4a;
    --teal: #005a80;
    --sky: #46a9e0;
    --light-sky: #87cff2;
    --ice: #e6f5fc;
    --mark: #3fa9de;
    --grey-text: #444b52;
    --white: #ffffff;
  }
  * { margin: 0; padding: 0; box-sizing: border-box; }
  html, body { width: 1200px; height: 970px; overflow: hidden; }
  body {
    position: relative;
    background: var(--backdrop);
    font-family: "Ubuntu", sans-serif;
  }
  .card {
    position: absolute;
    background: var(--card);
    box-shadow: 0 6px 18px rgba(0,0,0,0.45);
    overflow: hidden;
  }

  /* Front card */
  .card--front { left: 122px; top: 20px; width: 692px; height: 427px; }
  .brand {
    position: absolute;
    display: flex;
    align-items: center;
    gap: 22px;
  }
  .brand__dot { border-radius: 50%; background: var(--mark); flex: none; }
  .brand__name {
    font-family: "Ubuntu", sans-serif;
    font-weight: 700;
    color: var(--ink);
    line-height: 1;
  }
  .card--front .brand { left: 180px; top: 142px; }
  .card--front .brand__dot { width: 80px; height: 80px; }
  .card--front .brand__name { font-size: 82px; }
  .front__tagline {
    position: absolute;
    left: 0; right: 0; top: 283px;
    text-align: center;
    padding-right: 40px;
    font-size: 16px;
    color: var(--grey-text);
  }
  .colour-strip {
    position: absolute;
    left: 0; bottom: 0;
    width: 100%; height: 39px;
    display: flex;
  }
  .colour-strip span { display: block; height: 100%; }
  .colour-strip .s1 { width: 388px; background: var(--navy); }
  .colour-strip .s2 { width: 82px; background: var(--teal); }
  .colour-strip .s3 { width: 83px; background: var(--sky); }
  .colour-strip .s4 { width: 82px; background: var(--light-sky); }
  .colour-strip .s5 { flex: 1; background: var(--ice); }

  /* Back card */
  .card--back { left: 358px; top: 470px; width: 766px; height: 472px; }
  .card--back .brand { left: 30px; top: 212px; }
  .card--back .brand__dot { width: 76px; height: 76px; }
  .card--back .brand__name { font-size: 74px; }
  .contact-panel {
    position: absolute;
    left: 383px; top: 0;
    width: 383px; height: 100%;
  }
  .contact-panel__head {
    height: 157px;
    background: var(--navy);
    color: var(--white);
    text-align: center;
    padding-top: 14px;
  }
  .contact-panel__title {
    font-family: "Fira Sans Extra Condensed", sans-serif;
    font-weight: 600;
    font-size: 48px;
    line-height: 1.1;
  }
  .contact-panel__subtitle { font-size: 16.5px; margin-top: 2px; }
  .contact-row {
    position: relative;
    display: flex;
    align-items: center;
    padding-left: 12px;
  }
  .contact-row--phone { height: 93px; background: var(--teal); color: var(--white); }
  .contact-row--fax { height: 95px; background: var(--sky); color: var(--navy); }
  .contact-row--email { height: 95px; background: var(--light-sky); color: var(--navy); }
  .contact-row__end { height: 32px; background: var(--ice); }
  .contact-icon {
    width: 52px; height: 52px;
    border-radius: 50%;
    border: 2px solid currentColor;
    display: flex; align-items: center; justify-content: center;
    flex: none;
  }
  .contact-icon svg { width: 30px; height: 30px; }
  .contact-icon--at { font-size: 34px; font-weight: 500; line-height: 1; }
  .contact-text { margin-left: 22px; }
  .contact-row--phone .contact-text { font-size: 22px; letter-spacing: 1px; }
  .contact-row--fax .contact-text { font-size: 26px; font-weight: 700; margin-left: 24px; }
  .contact-row--email .contact-text { font-size: 21px; font-weight: 700; margin-left: 24px; }
</style>
</head>
<body>

  <section class="card card--front" aria-label="Front of business card">
    <div class="brand">
      <span class="brand__dot"></span>
      <span class="brand__name">b-ryx</span>
    </div>
    <p class="front__tagline">Building and Pest inspections</p>
    <div class="colour-strip">
      <span class="s1"></span><span class="s2"></span><span class="s3"></span><span class="s4"></span><span class="s5"></span>
    </div>
  </section>

  <section class="card card--back" aria-label="Back of business card">
    <div class="brand">
      <span class="brand__dot"></span>
      <span class="brand__name">b-ryx</span>
    </div>
    <div class="contact-panel">
      <header class="contact-panel__head">
        <h1 class="contact-panel__title">b-ryx prepurchase</h1>
        <p class="contact-panel__subtitle">Building and Pest inspections</p>
      </header>
      <div class="contact-row contact-row--phone">
        <span class="contact-icon" aria-label="Phone">
          <svg viewBox="0 0 24 24" fill="none" stroke="currentColor" stroke-width="1.6" stroke-linejoin="round">
            <path d="M16 3.5c1.6.4 2.6 1.2 3 2.2l-2.4 2.6-2-1.2C12.4 9 10 12.6 9.6 15.4l2 1.4-1.4 3.2C9 20 8 19.4 7.2 18.2 5.6 13 8.8 6.2 16 3.5z"/>
          </svg>
        </span>
        <span class="contact-text">0413926058</span>
      </div>
      <div class="contact-row contact-row--fax">
        <span class="contact-icon" aria-label="Fax">
          <svg viewBox="0 0 24 24" fill="none" stroke="currentColor" stroke-width="1.6">
            <rect x="7" y="3" width="10" height="7"/>
            <line x1="9" y1="5.5" x2="15" y2="5.5"/>
            <line x1="9" y1="7.8" x2="15" y2="7.8"/>
            <rect x="3" y="10" width="18" height="6" fill="currentColor"/>
            <rect x="3" y="16" width="18" height="5"/>
          </svg>
        </span>
        <span class="contact-text">02 93514770</span>
      </div>
      <div class="contact-row contact-row--email">
        <span class="contact-icon contact-icon--at" aria-label="Email">@</span>
        <span class="contact-text">b-ryx@mailnest.com.au</span>
      </div>
      <div class="contact-row__end"></div>
    </div>
  </section>

</body>
</html>
```